Business cards / Letterheads / Compliment slips

We are looking to get business cards, letterheads and compliment slips designed.

These will all have to follow the design of our new website and logo. Links to the website, logo and fonts can be found below...

The designs need to be simple with focus on the typography. Only the following colours should be used on the designs...

#7f9d3c
#191818
#fff

Website:
http://brightfieldweb.samplework.co.uk/

Logo:
https://www.filecrate.example/sh/9xk2mwq7tvbalp4/qrtuPL8NzK/logos

Fonts:
https://www.filecrate.example/sh/9xk2mwq7tvbalp4/Hw7ZpRt3sQ/Fonts/BayerModern_TTF

and

https://www.filecrate.example/sh/9xk2mwq7tvbalp4/T6nVyo4Dc1/Fonts/MuseoSansFamily

Reason: We would like some more design submissions

Reason: We are still deciding on designs we like and would like to see some more submissions...

Industry/Entity Type

Business

Requirements
Must have
• The designs need to be simple with focus on the typography. Only the following colours should be used on the designs...

#7f9d3c
#191818
#fff
Should not have
• - Any fonts that are not provided.
- Any colours that are not provided.

```html
<!DOCTYPE html>
<html lang="en">
<head>
<meta charset="utf-8">
<title>brightfieldweb stationery</title>
<link href="https://fonts.googleapis.com/css2?family=Nunito+Sans:wght@300;400;600;700&display=swap" rel="stylesheet">
<style>
  :root {
    --green: #7f9d3c;
    --ink: #191818;
    --band: #323232;
    --paper: #ffffff;
    --stage: #e4e4e2;
    --muted: #555;
  }
  * { box-sizing: border-box; margin: 0; padding: 0; }
  html, body { width: 1200px; height: 1003px; overflow: hidden; }
  body {
    background: var(--stage);
    font-family: "Nunito Sans", Arial, sans-serif;
    color: var(--ink);
    position: relative;
  }
  .sheet {
    position: absolute;
    background: var(--paper);
    box-shadow: 0 4px 14px rgba(0,0,0,.18);
    overflow: hidden;
  }
  .band { background: var(--band); position: relative; }
  .brand {
    display: flex; align-items: center; gap: 8px;
    color: var(--paper); font-weight: 700; letter-spacing: -0.2px;
  }
  .brand-dot { border-radius: 50%; background: var(--green); flex: none; }
  .url { color: var(--muted); font-weight: 300; }
  .url b { color: var(--green); font-weight: 600; }
  .band .url { color: #bbb; }
  .address { font-weight: 300; line-height: 1.3; }
  .address .office { color: var(--green); font-weight: 400; }
  .address .phone { color: var(--green); font-weight: 600; margin-top: 6px; }

  /* Letterhead */
  .letterhead { left: 40px; top: 100px; width: 560px; height: 792px; }
  .letterhead .band { height: 96px; }
  .letterhead .brand { position: absolute; left: 28px; bottom: 16px; font-size: 26px; }
  .letterhead .brand-dot { width: 22px; height: 22px; }
  .letterhead .url { position: absolute; right: 26px; top: 16px; font-size: 11px; }
  .letterhead .address {
    position: absolute; right: 30px; top: 450px; text-align: right; font-size: 13px;
  }
  .letterhead .address .phone { font-size: 17px; }

  /* Compliment slip */
  .slip { left: 640px; top: 100px; width: 520px; height: 248px; }
  .slip .band { height: 52px; }
  .slip .brand { position: absolute; left: 20px; bottom: 10px; font-size: 20px; }
  .slip .brand-dot { width: 17px; height: 17px; }
  .slip .title {
    position: absolute; right: 20px; top: 64px;
    color: var(--green); font-size: 21px; font-weight: 300;
  }
  .slip .url { position: absolute; right: 20px; top: 100px; font-size: 10px; }
  .slip .address { position: absolute; left: 20px; bottom: 18px; font-size: 11px; }
  .slip .address .phone { font-size: 15px; margin-top: 4px; }

  /* Business cards */
  .card { top: 390px; width: 250px; height: 162px; }
  .card-front { left: 640px; }
  .card-front .band { height: 62px; }
  .card-front .brand { position: absolute; right: 12px; top: 10px; font-size: 15px; }
  .card-front .brand-dot { width: 13px; height: 13px; }
  .card-front .person { position: absolute; left: 12px; bottom: 7px; }
  .person .name { color: var(--green); font-size: 13px; font-weight: 400; }
  .person .role { color: #ddd; font-size: 8px; font-weight: 300; }
  .card-front .address { position: absolute; left: 12px; bottom: 12px; font-size: 8px; }
  .card-front .address .phone { font-size: 11px; margin-top: 3px; }
  .card-front .url { position: absolute; right: 12px; bottom: 14px; font-size: 7.5px; }

  .card-back { left: 910px; background: var(--band); }
  .card-back .brand {
    position: absolute; left: 22px; top: 48px; font-size: 22px;
  }
  .card-back .brand-dot { width: 30px; height: 30px; }
  .card-back .tagline {
    position: absolute; left: 22px; top: 98px; color: #ddd;
    font-size: 10px; font-weight: 300; line-height: 1.35;
  }
  .card-back .tagline b { color: var(--green); font-weight: 400; }
</style>
</head>
<body>

  <section class="sheet letterhead" aria-label="Letterhead">
    <header class="band">
      <div class="brand"><span class="brand-dot"></span>brightfieldweb</div>
      <div class="url">www.<b>brightfieldweb</b>.co.uk</div>
    </header>
    <address class="address" style="font-style:normal">
      <div class="office">Ashbury Head Office</div>
      <div>Floor 3,</div>
      <div>24 Fernhill Road,</div>
      <div>Ashbury,</div>
      <div>AB1 2CD</div>
      <div class="phone">0800 555 0142</div>
      <div>hello@brightfieldweb.co.uk</div>
    </address>
  </section>

  <section class="sheet slip" aria-label="Compliment slip">
    <header class="band">
      <div class="brand"><span class="brand-dot"></span>brightfieldweb</div>
    </header>
    <div class="title">With Compliments</div>
    <div class="url">www.<b>brightfieldweb</b>.co.uk</div>
    <address class="address" style="font-style:normal">
      <div class="office">Ashbury Head Office</div>
      <div>Floor 3,</div>
      <div>24 Fernhill Road,</div>
      <div>Ashbury,</div>
      <div>AB1 2CD</div>
      <div class="phone">0800 555 0142</div>
      <div>hello@brightfieldweb.co.uk</div>
    </address>
  </section>

  <section class="sheet card card-front" aria-label="Business card front">
    <header class="band">
      <div class="brand"><span class="brand-dot"></span>brightfieldweb</div>
      <div class="person">
        <div class="name">Daniel Marsh</div>
        <div class="role">General manager</div>
      </div>
    </header>
    <address class="address" style="font-style:normal">
      <div class="office">Ashbury Head Office</div>
      <div>Floor 3,</div>
      <div>24 Fernhill Road,</div>
      <div>Ashbury,</div>
      <div>AB1 2CD</div>
      <div class="phone">0800 555 0142</div>
      <div>hello@brightfieldweb.co.uk</div>
    </address>
    <div class="url">www.<b>brightfieldweb</b>.co.uk</div>
  </section>

  <section class="sheet card card-back" aria-label="Business card back">
    <div class="brand"><span class="brand-dot"></span>brightfieldweb</div>
    <p class="tagline">Climb the search engine ranks<br>for higher <b>profits</b></p>
  </section>

</body>
</html>
```